Business Card Design.

Life and Wellness Coach
www.brightpathwell.net
Want to use my name as the logo it could be the initials TRK or my full name. I want to trade mark me.
I like clean lines and simple designs, but it pops using the colors scheme (one or two colors) on the website.
I provide life and health coaching virtually and in person. My services include: Dietary Signal Screening, Sensitivity Clearing Review, Wellness Coaching, Life Coaching. Life and Health Assessments, and I sell foundational health products and specialized nutrition. Use colors that represent healing and trust.
Target Market(s)
Women for the ages of 30 - 60
Industry/Entity Type
Health
Contact Information for Business Card
Tessa Rosalind Kimble
Life and Wellness Coach
tessa@coachtrk.net
www.brightpathwell.net
555-217-8364
Health is not an event it's a lifestyle (tag line or if you have a better tag line)

```html
<!DOCTYPE html>
<html lang="en">
<head>
<meta charset="utf-8">
<title>Tessa Rosalind Kimble – Business Card</title>
<link rel="stylesheet" href="https://fonts.googleapis.com/css2?family=Lato:wght@400;700&family=Lora:ital@1&display=swap">
<style>
  :root {
    --stage: #232323;
    --card-white: #ffffff;
    --card-white-edge: #ececec;
    --berry: #a02a5f;
    --berry-deep: #7c1b49;
    --rose-ink: #b7477c;
    --slate: #3d4450;
    --soft-white: #f6e9ef;
    --photo-warm: #6b3a2c;
    --photo-light: #d9b7a3;
    --photo-blue: #233f9c;
  }
  * { box-sizing: border-box; margin: 0; padding: 0; }
  html, body { width: 1200px; height: 873px; overflow: hidden; }
  body {
    background: var(--stage);
    display: flex;
    align-items: center;
    justify-content: center;
    gap: 40px;
    font-family: "Lato", sans-serif;
  }
  .card {
    width: 540px;
    height: 315px;
    border-radius: 18px;
    position: relative;
    overflow: hidden;
    box-shadow: 0 12px 30px rgba(0,0,0,.5);
  }

  /* Front */
  .card-front {
    background: linear-gradient(160deg, var(--card-white) 60%, var(--card-white-edge));
  }
  .portrait {
    position: absolute;
    left: 0; top: 0; bottom: 0;
    width: 46%;
    background:
      radial-gradient(ellipse 40% 45% at 50% 42%, var(--photo-light), transparent 70%),
      linear-gradient(180deg, var(--photo-warm) 0%, #8a4f3c 55%, var(--photo-blue) 100%);
  }
  .front-brand {
    position: absolute;
    left: 50%; right: 22px; top: 62px;
    text-align: center;
  }
  .front-brand .name {
    font-family: "Lato", sans-serif;
    font-weight: 400;
    font-size: 34px;
    line-height: 1.2;
    color: var(--rose-ink);
  }
  .rule-title {
    display: flex;
    align-items: center;
    gap: 8px;
    margin-top: 12px;
    font-size: 12px;
    font-weight: 700;
    color: var(--slate);
    white-space: nowrap;
  }
  .rule-title::before, .rule-title::after {
    content: "";
    flex: 1;
    height: 2px;
    background: var(--rose-ink);
  }

  /* Back */
  .card-back {
    background: linear-gradient(160deg, var(--berry) 0%, var(--berry-deep) 100%);
    color: var(--soft-white);
  }
  .back-brand {
    position: absolute;
    left: 120px; right: 30px; top: 26px;
    text-align: center;
  }
  .back-brand .name {
    font-family: "Lato", sans-serif;
    font-weight: 400;
    font-size: 26px;
    line-height: 1.1;
    color: var(--card-white);
  }
  .back-brand .rule-title { color: var(--card-white); font-size: 14px; margin-top: 6px; }
  .back-brand .rule-title::before, .back-brand .rule-title::after { background: var(--slate); }

  .services {
    position: absolute;
    left: 300px; top: 112px;
  }
  .services h2 {
    font-size: 13px;
    font-weight: 700;
    text-decoration: underline;
    letter-spacing: .3px;
    margin-bottom: 6px;
  }
  .services ul { list-style: none; }
  .services li {
    font-size: 13px;
    line-height: 1.55;
    padding-left: 14px;
    position: relative;
  }
  .services li::before {
    content: "";
    position: absolute;
    left: 2px; top: 8px;
    width: 6px; height: 6px;
    border-radius: 50%;
    background: var(--soft-white);
  }

  .contacts {
    position: absolute;
    left: 26px; top: 176px;
    list-style: none;
  }
  .contacts li {
    display: flex;
    align-items: center;
    gap: 8px;
    font-size: 14px;
    font-weight: 700;
    margin-bottom: 8px;
  }
  .contact-icon {
    width: 22px; height: 22px;
    border-radius: 50%;
    background: var(--soft-white);
    display: flex; align-items: center; justify-content: center;
  }
  .tagline {
    position: absolute;
    left: 0; right: 0; bottom: 22px;
    text-align: center;
    font-family: "Lora", serif;
    font-style: italic;
    font-size: 17px;
    color: #e3c9d6;
  }
</style>
</head>
<body>

  <section class="card card-front">
    <div class="portrait" role="img" aria-label="Portrait photo of the coach"></div>
    <div class="front-brand">
      <div class="name">Tessa<br>Rosalind Kimble</div>
      <div class="rule-title">Life and Wellness Coach</div>
    </div>
  </section>

  <section class="card card-back">
    <div class="back-brand">
      <div class="name">Tessa Rosalind Kimble</div>
      <div class="rule-title">Life and Wellness Coach</div>
    </div>

    <div class="services">
      <h2>OUR SERVICES</h2>
      <ul>
        <li>Life Coaching</li>
        <li>Wellness Coaching</li>
        <li>Dietary Signal Screening</li>
        <li>Sensitivity Clearing Review</li>
        <li>Life &amp; Health Assessments</li>
      </ul>
    </div>

    <ul class="contacts">
      <li>
        <span class="contact-icon">
          <svg width="12" height="14" viewBox="0 0 12 14"><rect x="2" y="1" width="8" height="12" rx="1.5" fill="none" stroke="#7c1b49" stroke-width="1.6"/><circle cx="6" cy="10.5" r=".9" fill="#7c1b49"/></svg>
        </span>555-217-8364
      </li>
      <li>
        <span class="contact-icon">
          <svg width="13" height="10" viewBox="0 0 13 10"><rect x="1" y="1" width="11" height="8" fill="none" stroke="#7c1b49" stroke-width="1.4"/><path d="M1 1 L6.5 5.5 L12 1" fill="none" stroke="#7c1b49" stroke-width="1.4"/></svg>
        </span>tessa@coachtrk.net
      </li>
      <li>
        <span class="contact-icon">
          <svg width="13" height="13" viewBox="0 0 13 13"><rect x="1" y="5" width="7" height="4" rx="2" transform="rotate(-45 4.5 7)" fill="none" stroke="#7c1b49" stroke-width="1.5"/><rect x="5" y="4" width="7" height="4" rx="2" transform="rotate(-45 8.5 6)" fill="none" stroke="#7c1b49" stroke-width="1.5"/></svg>
        </span>www.brightpathwell.net
      </li>
    </ul>

    <p class="tagline">Health is not an event it's a lifestyle</p>
  </section>

</body>
</html>
```